Copper and Slate Mists NZ new website!

We are a new online vaping retailer and are looking for an awesome sleek website. We are going to be selling a variety of vaping products and gear. Our logo has just been developed and we would like to keep the website in line with the black, tan a white theme. We would like to trying watermarking or imposing the rottie into the background of the website on the home page, with the page being black and you can see the tan and white colours only.

Coding

Coded - Design and coding required

Number of Pages Required

2 page

Font styles to use
Serif
Sans Serif
Decorative

Requirements
Must have
• A home page and a standard page for products
• Stay in line with the colours in the logo

```html
<!DOCTYPE html>
<html lang="en">
<head>
<meta charset="utf-8">
<title>Copper and Slate Mists NZ</title>
<link rel="stylesheet" href="https://fonts.googleapis.com/css2?family=Lora:wght@400;700&family=Open+Sans:wght@400;600;700&display=swap">
<style>
:root{
  --black:#000;
  --band:#1f1f1f;
  --footer:#181512;
  --white:#fff;
  --grey:#bdbdbd;
  --tan:#c8731f;
  --price:#3d9be0;
  --serif:'Lora', Georgia, serif;
  --sans:'Open Sans', Arial, sans-serif;
}
*{box-sizing:border-box;margin:0;padding:0}
html,body{width:1200px;height:3258px;overflow:hidden;background:var(--black)}
body{position:relative;font-family:var(--sans);color:var(--white)}
.abs{position:absolute}

/* header */
.site-header{position:absolute;left:0;top:0;width:1200px;height:171px;background:var(--black)}
.lang{left:212px;top:14px;font-size:11px;color:var(--grey)}
.search{left:212px;top:55px;width:190px;height:27px;border:1px solid #555;background:#0a0a0a;font-size:11px;color:var(--grey);padding:5px 8px}
.search svg{position:absolute;right:7px;top:7px}
.account{top:15px;font-size:11px;color:var(--grey);letter-spacing:.5px}
.cart{left:931px;top:60px;font-size:11px;color:var(--grey)}
.cart b{display:inline-block;width:14px;height:14px;border-radius:50%;background:var(--tan);color:#fff;font-size:9px;text-align:center;line-height:14px;margin-left:3px;vertical-align:top}
.nav-item{top:124px;font-family:var(--serif);font-size:12px;font-weight:700;text-transform:uppercase;white-space:nowrap}
.brand{left:500px;top:8px;width:200px;text-align:center}
.brand-mark{display:block;width:88px;height:88px;border-radius:50%;background:var(--tan);margin:0 auto 6px}
.brand-name{display:block;font-family:var(--serif);font-size:13px;font-weight:700;color:var(--white);white-space:nowrap}

/* hero */
.hero{left:0;top:171px;width:1200px;height:407px;background:linear-gradient(90deg,#2a2a2a,#141414 60%,#0c0c0c)}
.hero-media{left:163px;width:517px;height:350px;background:radial-gradient(ellipse at 45% 55%,#8d8d8d 0,#5a3d33 35%,#2a2a2a 75%);border-radius:4px}
.hero-title{left:700px;font-family:var(--serif);font-size:38px;line-height:1.25;font-weight:700}
.btn{display:inline-block;font-family:var(--sans);font-weight:700;text-transform:uppercase;text-align:center}
.btn-dark{background:var(--black);color:var(--white);border:1px solid #444}
.btn-light{background:var(--white);color:var(--black)}

/* dark backdrop */
.backdrop{left:0;top:578px;width:1200px;height:888px;background:radial-gradient(ellipse at 40% 50%,#4a3220 0,#2a1d14 40%,#120d09 80%)}
.backdrop.latest{top:1824px;height:641px;background:radial-gradient(ellipse at 45% 40%,#3d2a1c 0,#251a12 45%,#100b08 85%)}

.section-title{left:0;width:1200px;text-align:center;font-family:var(--serif);font-size:24px;font-weight:700;letter-spacing:1px}
.rule{height:1px;background:#6b5a4a;width:280px}
.intro{left:300px;width:600px;text-align:center;font-size:13px;line-height:1.9;color:#ddd}

.card{width:185px;text-align:center}
.card-img{width:185px;height:210px;background:var(--white);display:flex;align-items:center;justify-content:center}
.card-img div{width:130px;height:160px;border-radius:4px}
.card-name{margin-top:26px;font-family:var(--serif);font-size:14px;font-weight:700;text-transform:uppercase;white-space:nowrap}
.card-desc{margin-top:6px;height:36px;font-size:11px;line-height:1.6;color:#ddd}
.card-price{margin-top:8px;font-size:15px;color:var(--price)}
.card-btn{margin-top:8px;font-size:9px;padding:5px 12px;background:var(--black);border:1px solid #555}
.arrow{width:30px;height:54px;background:rgba(70,70,70,.75);display:flex;align-items:center;justify-content:center}

.brand-row{left:170px;top:1322px;width:860px;display:flex;justify-content:space-between;align-items:center}
.brand-word{font-family:var(--serif);font-weight:700;color:var(--white);font-size:30px;letter-spacing:1px}

/* best sellers */
.bestsellers{left:0;top:1466px;width:1200px;height:358px;background:linear-gradient(90deg,#6a6a6a 0,#3b3b3b 35%,#1c1c1c 60%,#8a6a55 100%)}
.bs-title{left:0;width:1200px;top:1560px;text-align:center;font-family:var(--serif);font-size:36px}
.bs-sub{left:0;width:1200px;top:1614px;text-align:center;font-size:15px}

/* features */
.features{left:0;top:2465px;width:1200px;height:272px;background:var(--band)}
.feature{width:280px;text-align:center}
.feature h3{margin-top:14px;font-family:var(--serif);font-size:16px;font-weight:700}
.feature p{margin-top:12px;font-size:12px;line-height:1.6;color:#ddd}

/* footer */
.footer{left:0;top:2737px;width:1200px;height:439px;background:var(--footer)}
.foot-h{top:2814px;font-size:18px;font-weight:700}
.foot-line{top:2848px;height:1px;background:#555}
.contact-row{font-size:12px;line-height:1.7;color:#ddd}
.contact-row svg{position:absolute;left:-1px;top:3px}
.social{top:3010px;width:14px;height:14px;border-radius:50%;background:#ddd}
.field{left:400px;width:196px;background:#fff;border:1px solid #ccc;color:#999;font-size:11px;padding:6px 8px}
.submit{left:400px;top:3060px;width:196px;height:30px;background:var(--tan);color:#fff;font-size:12px;font-weight:700;text-align:center;line-height:30px}
.links{left:626px;top:2880px;font-size:12px;line-height:1.62;color:#eee;list-style:none}
.map{left:832px;top:2880px;width:186px;height:112px;background:linear-gradient(135deg,#e9e5dc,#d8e6d2 50%,#cfdde8);border-radius:2px}
.bottom{left:0;top:3176px;width:1200px;height:82px;background:#0e0c0a;border-top:1px solid #333}
.copy{left:183px;top:3190px;font-size:12px;color:#aaa}
.to-top{left:1030px;top:3184px;width:30px;height:30px;background:var(--tan);display:flex;align-items:center;justify-content:center}
</style>
</head>
<body>

<header class="site-header">
  <div class="abs lang">EN ▾</div>
  <div class="abs search">Search
    <svg width="12" height="12" viewBox="0 0 12 12"><circle cx="5" cy="5" r="3.6" stroke="#ddd" stroke-width="1.5" fill="none"/><line x1="7.6" y1="7.6" x2="11" y2="11" stroke="#ddd" stroke-width="1.5"/></svg>
  </div>
  <div class="abs account" style="left:823px">♡ WISHLIST</div>
  <div class="abs account" style="left:905px">SIGN IN</div>
  <div class="abs account" style="left:968px">REGISTER</div>
  <div class="abs cart">Cart<b>0</b></div>

  <nav>
    <div class="abs nav-item" style="left:209px">New</div>
    <div class="abs nav-item" style="left:263px">Brands</div>
    <div class="abs nav-item" style="left:333px">Starter Kit</div>
    <div class="abs nav-item" style="left:440px">Devices</div>
    <div class="abs nav-item" style="left:714px">Atomizers</div>
    <div class="abs nav-item" style="left:800px">Tanks</div>
    <div class="abs nav-item" style="left:858px">Accessories</div>
    <div class="abs nav-item" style="left:968px">E-Liquids</div>
  </nav>

  <div class="abs brand">
    <span class="brand-mark"></span>
    <span class="brand-name">Copper and Slate Mists NZ</span>
  </div>
</header>

<section>
  <div class="abs hero"></div>
  <div class="abs hero-media" style="top:201px" role="img" aria-label="Box mod vaping devices with tanks and a slim pen, surrounded by soft vapour"></div>
  <h1 class="abs hero-title" style="top:263px">Variety of vaping<br>products and gear</h1>
  <a class="abs btn btn-dark" style="left:785px;top:398px;width:150px;height:40px;line-height:38px;font-size:11px">Shop Now</a>
</section>

<div class="abs backdrop" role="img" aria-label="Dark watermark of the brand's dog mascot in tan and black tones"></div>

<section>
  <div class="abs rule" style="left:171px;top:652px"></div>
  <div class="abs rule" style="left:749px;top:652px"></div>
  <h2 class="abs section-title" style="top:636px">FEATURED PRODUCTS</h2>
  <p class="abs intro" style="top:688px">Quis autem vel eum iure reprehenderit qui in ea voluptate velit esse quam nihil molestiae consequatur vel illum qui dolorem eum fugiat quo voluptas nulla pariatur</p>

  <div class="abs arrow" style="left:103px;top:956px"><svg width="10" height="16"><path d="M8 1 2 8l6 7" stroke="#fff" stroke-width="2" fill="none"/></svg></div>
  <div class="abs arrow" style="left:1067px;top:956px"><svg width="10" height="16"><path d="M2 1l6 7-6 7" stroke="#fff" stroke-width="2" fill="none"/></svg></div>

  <article class="abs card" style="left:171px;top:782px">
    <div class="card-img"><div role="img" aria-label="Squonk box mod kit in red and black" style="background:linear-gradient(135deg,#5a2a22,#1b1b1b 60%,#8a4a32)"></div></div>
    <h3 class="card-name">Vantor Vape</h3>
    <p class="card-desc">Vantor Arc Squonk Kit<br>Limited Run</p>
    <p class="card-price">$64.95</p>
    <span class="btn card-btn">Add to cart</span>
  </article>
  <article class="abs card" style="left:391px;top:782px">
    <div class="card-img"><div role="img" aria-label="Three slim pod system devices in blue, red and black" style="background:linear-gradient(90deg,#1f6fd1 0 33%,#d12a2a 33% 66%,#222 66%)"></div></div>
    <h3 class="card-name">Aspira</h3>
    <p class="card-desc">Aspira Solo Pod Starter<br>Kit</p>
    <p class="card-price">$18.95</p>
    <span class="btn card-btn">Add to cart</span>
  </article>
  <article class="abs card" style="left:612px;top:782px">
    <div class="card-img"><div role="img" aria-label="Red concentrate vaporizer kit" style="background:linear-gradient(160deg,#d8262c,#8c1519 70%,#333)"></div></div>
    <h3 class="card-name">Cartova</h3>
    <p class="card-desc">Cartova Compact Concentrate<br>Vaporizer Kit</p>
    <p class="card-price">$20.95</p>
    <span class="btn card-btn">Add to cart</span>
  </article>
  <article class="abs card" style="left:832px;top:782px">
    <div class="card-img"><div role="img" aria-label="Clear disposable sub-ohm tanks" style="background:linear-gradient(180deg,#c9d2d6,#8c979c 60%,#e4e8ea)"></div></div>
    <h3 class="card-name">Clearview</h3>
    <p class="card-desc">Nerdmist Clearview<br>Disposable Tank</p>
    <p class="card-price">$27.99</p>
    <span class="btn card-btn">Add to cart</span>
  </article>
</section>

<section>
  <h2 class="abs section-title" style="top:1210px">FEATURED BRANDS</h2>
  <div class="abs brand-row">
    <span class="brand-word">NORDVAP</span>
    <span class="brand-word">KELPA</span>
    <span class="brand-word">RIVERTON</span>
    <span class="brand-word">ASHCLOUD</span>
    <span class="brand-word">TEMPLO</span>
  </div>
</section>

<section>
  <div class="abs bestsellers" role="img" aria-label="Hand holding a slim vape pen while exhaling a cloud of vapour"></div>
  <h2 class="abs bs-title">Our Best Sellers</h2>
  <p class="abs bs-sub">The Latest and Greatest Collections</p>
  <a class="abs btn btn-light" style="left:515px;top:1664px;width:170px;height:38px;line-height:38px;font-size:13px">Shop Now</a>
</section>

<div class="abs backdrop latest" role="img" aria-label="Dark watermark of the brand's dog mascot in tan and black tones"></div>

<section>
  <div class="abs rule" style="left:171px;top:1898px"></div>
  <div class="abs rule" style="left:749px;top:1898px"></div>
  <h2 class="abs section-title" style="top:1882px">LATEST PRODUCTS</h2>
  <p class="abs intro" style="top:1934px">Quis autem vel eum iure reprehenderit qui in ea voluptate velit esse quam nihil molestiae consequatur vel illum qui dolorem eum fugiat quo voluptas nulla pariatur</p>

  <div class="abs arrow" style="left:103px;top:2212px"><svg width="10" height="16"><path d="M8 1 2 8l6 7" stroke="#fff" stroke-width="2" fill="none"/></svg></div>
  <div class="abs arrow" style="left:1067px;top:2212px"><svg width="10" height="16"><path d="M2 1l6 7-6 7" stroke="#fff" stroke-width="2" fill="none"/></svg></div>

  <article class="abs card" style="left:171px;top:2031px">
    <div class="card-img"><div role="img" aria-label="E-liquid bottle with box" style="background:linear-gradient(135deg,#e05a5a,#f3c9c0 50%,#c0392b)"></div></div>
    <h3 class="card-name">Breeze E-Liquids</h3>
    <p class="card-desc">Berry Chill - Breeze Works<br>E-Liquid - 100ml</p>
    <p class="card-price">$18.95</p>
    <span class="btn card-btn">Add to cart</span>
  </article>
  <article class="abs card" style="left:391px;top:2031px">
    <div class="card-img"><div role="img" aria-label="Slim pod system device with box" style="background:linear-gradient(160deg,#e8e8e8,#9a9a9a 55%,#c0392b)"></div></div>
    <h3 class="card-name">Sorvin</h3>
    <p class="card-desc">Sorvin Slim Pod System</p>
    <p class="card-price">$18.95</p>
    <span class="btn card-btn">Add to cart</span>
  </article>
  <article class="abs card" style="left:612px;top:2031px">
    <div class="card-img"><div role="img" aria-label="Red concentrate vaporizer kit" style="background:linear-gradient(160deg,#d8262c,#8c1519 70%,#333)"></div></div>
    <h3 class="card-name">Cartova</h3>
    <p class="card-desc">Cartova Compact Concentrate<br>Vaporizer Kit</p>
    <p class="card-price">$20.95</p>
    <span class="btn card-btn">Add to cart</span>
  </article>
  <article class="abs card" style="left:832px;top:2031px">
    <div class="card-img"><div role="img" aria-label="Two vape pens in silver and black" style="background:linear-gradient(90deg,#cfcfcf 0 50%,#2a2a2a 50%)"></div></div>
    <h3 class="card-name">Vape Pens</h3>
    <p class="card-desc">Aut reiciendis voluptatibus<br>alias consequatur</p>
    <p class="card-price">$27.99</p>
    <span class="btn card-btn">Add to cart</span>
  </article>
</section>

<section>
  <div class="abs features"></div>
  <div class="abs feature" style="left:172px;top:2522px">
    <svg width="46" height="34" viewBox="0 0 46 34"><path d="M2 4h26v20H2zM28 11h9l7 7v6H28z" fill="none" stroke="#fff" stroke-width="2"/><circle cx="10" cy="27" r="4" fill="#1f1f1f" stroke="#fff" stroke-width="2"/><circle cx="36" cy="27" r="4" fill="#1f1f1f" stroke="#fff" stroke-width="2"/></svg>
    <h3>Fast Delivery</h3>
    <p>Nemo enim ipsam voluptatem quia voluptas sit aspernatur aut odit aut fugit sed quia consequuntur magni</p>
  </div>
  <div class="abs feature" style="left:460px;top:2522px">
    <svg width="40" height="34" viewBox="0 0 40 34"><path d="M2 3h6l5 20h20l4-14H11" fill="none" stroke="#fff" stroke-width="2"/><circle cx="15" cy="29" r="3" fill="#fff"/><circle cx="30" cy="29" r="3" fill="#fff"/><path d="M17 14l4 4 7-7" fill="none" stroke="#fff" stroke-width="2"/></svg>
    <h3>Secure Checkout</h3>
    <p>Nemo enim ipsam voluptatem quia voluptas sit aspernatur aut odit aut fugit sed quia consequuntur magni</p>
  </div>
  <div class="abs feature" style="left:752px;top:2522px">
    <svg width="40" height="34" viewBox="0 0 40 34"><path d="M4 14h32v18H4zM2 8h36v6H2zM20 8v24" fill="none" stroke="#fff" stroke-width="2"/><path d="M20 8c-4-7-12-6-10 0M20 8c4-7 12-6 10 0" fill="none" stroke="#fff" stroke-width="2"/></svg>
    <h3>Free Returns</h3>
    <p>Nemo enim ipsam voluptatem quia voluptas sit aspernatur aut odit aut fugit sed quia consequuntur magni</p>
  </div>
</section>

<footer>
  <div class="abs footer"></div>

  <h4 class="abs foot-h" style="left:180px">Contact Us</h4>
  <div class="abs foot-line" style="left:180px;width:170px"></div>
  <div class="abs contact-row" style="top:2882px;padding-left:22px;left:180px;width:200px">
    <svg width="10" height="13" viewBox="0 0 10 13"><path d="M5 0a5 5 0 0 1 5 5c0 3-5 8-5 8S0 8 0 5a5 5 0 0 1 5-5z" fill="#fff"/><circle cx="5" cy="5" r="2" fill="#181512"/></svg>
    152, voluptates repudiandae<br>sint et molestiae non
  </div>
  <div class="abs contact-row" style="top:2936px;padding-left:22px;left:180px">
    <svg width="12" height="12" viewBox="0 0 12 12"><path d="M2 0h3l1 3-2 1a7 7 0 0 0 4 4l1-2 3 1v3c0 1-1 2-2 2A10 10 0 0 1 0 2c0-1 1-2 2-2z" fill="#fff"/></svg>
    (02) 1111 2222
  </div>
  <div class="abs contact-row" style="top:2972px;padding-left:22px;left:180px">
    <svg width="13" height="10" viewBox="0 0 13 10"><rect width="13" height="10" fill="#fff"/><path d="M0 0l6.5 5L13 0" stroke="#181512" fill="none"/></svg>
    info@copperslate.example
  </div>
  <span class="abs social" style="left:206px"></span>
  <span class="abs social" style="left:232px"></span>
  <span class="abs social" style="left:258px"></span>
  <span class="abs social" style="left:286px"></span>

  <h4 class="abs foot-h" style="left:400px">Quick Contact</h4>
  <div class="abs foot-line" style="left:400px;width:196px"></div>
  <div class="abs field" style="top:2880px;height:28px">Name...</div>
  <div class="abs field" style="top:2915px;height:28px">Email...</div>
  <div class="abs field" style="top:2950px;height:100px">Message...</div>
  <div class="abs submit">Submit</div>

  <h4 class="abs foot-h" style="left:626px">Links</h4>
  <div class="abs foot-line" style="left:626px;width:80px"></div>
  <ul class="abs links">
    <li>Best Vapes</li>
    <li>MyMistPro Prime Membership</li>
    <li>COUPON CODE</li>
    <li>Blog</li>
    <li>WHOLESALE</li>
    <li>AFFILIATE PROGRAM</li>
    <li>TERMS &amp; CONDITIONS</li>
    <li>WARRANTY &amp; RETURNS</li>
    <li>CONTACT US</li>
    <li>PRIVACY POLICY</li>
    <li>Sitemap</li>
  </ul>

  <h4 class="abs foot-h" style="left:838px">Locate Us</h4>
  <div class="abs foot-line" style="left:832px;width:100px"></div>
  <div class="abs map" role="img" aria-label="Street map showing the store location"></div>

  <div class="abs bottom"></div>
  <p class="abs copy">©Copyright Information here</p>
  <div class="abs to-top"><svg width="12" height="8"><path d="M1 7l5-5 5 5" stroke="#fff" stroke-width="2" fill="none"/></svg></div>
</footer>

</body>
</html>
```